Online Psychology Practice needs business cards.

Online Psychology service needs business cards. Have own logo- please see uploaded. I have other file formats if you need (not sure one needed?)

Details for Business Card:
Fiona Kettlewood
Clinical Psychologist BPsych, BPsych (Hons), MPsych (Clin), MAPS
T: 0457260714 | F: 08 71526804
E: hello@harbourlightmindcarestudio.com.au
W: harbourlightmindcarestudio.com.au

Industry/Entity Type

Health

Contact Information for Business Card

Logo plus details above (couldn't write in this section)

```html
<!DOCTYPE html>
<html lang="en">
<head>
<meta charset="utf-8">
<title>Harbourlight Mindcare Studio – Business Card</title>
<link rel="stylesheet" href="https://fonts.googleapis.com/css2?family=Cinzel:wght@600&family=Mulish:wght@400;500&display=swap">
<style>
  :root {
    --page: #ffffff;
    --card: #ffffff;
    --navy: #1d5486;
    --teal: #5aaac4;
    --pattern-pale: #e6edf3;
    --white: #ffffff;
    --shadow: rgba(0, 0, 0, 0.16);
  }
  * { box-sizing: border-box; margin: 0; padding: 0; }
  html, body {
    width: 1200px;
    height: 1200px;
    overflow: hidden;
    background: var(--page);
  }
  .canvas {
    position: relative;
    width: 1200px;
    height: 1200px;
  }
  .card {
    position: absolute;
    left: 184px;
    width: 830px;
    height: 473px;
    background: var(--card);
    box-shadow: 4px 10px 22px var(--shadow);
    overflow: hidden;
  }
  .card--front { top: 91px; }
  .card--back { top: 633px; }

  /* Front */
  .front-pattern {
    position: absolute;
    top: 0;
    right: 0;
    width: 205px;
    height: 100%;
    background: linear-gradient(90deg, rgba(230,237,243,0) 0%, var(--pattern-pale) 45%, var(--pattern-pale) 100%);
  }
  .brand {
    position: absolute;
    left: 70px;
    top: 130px;
    display: flex;
    align-items: center;
    gap: 72px;
  }
  .brand__mark {
    width: 200px;
    height: 200px;
    border-radius: 50%;
    background: var(--navy);
    flex: none;
  }
  .brand__name {
    font-family: "Cinzel", serif;
    font-weight: 600;
    font-size: 24px;
    line-height: 1.25;
    letter-spacing: 1px;
    color: var(--navy);
    text-align: center;
  }

  /* Back */
  .back-header {
    position: absolute;
    top: 0;
    left: 0;
    width: 100%;
    height: 137px;
  }
  .holder-name {
    position: absolute;
    right: 62px;
    top: 45px;
    font-family: "Cinzel", serif;
    font-weight: 600;
    font-size: 33px;
    color: var(--navy);
    letter-spacing: 0.5px;
  }
  .back-band {
    position: absolute;
    top: 137px;
    left: 0;
    width: 100%;
    height: 336px;
    background: var(--teal);
  }
  .credentials {
    position: absolute;
    left: 65px;
    top: 172px;
    font-family: "Mulish", sans-serif;
    font-weight: 500;
    font-size: 20px;
    line-height: 27.5px;
    color: var(--white);
  }
  .divider {
    position: absolute;
    left: 65px;
    top: 295px;
    width: 71px;
    height: 2px;
    background: var(--white);
  }
  .contacts {
    position: absolute;
    left: 65px;
    top: 356px;
    list-style: none;
    font-family: "Mulish", sans-serif;
    font-size: 19px;
    color: var(--white);
  }
  .contacts li {
    display: flex;
    align-items: center;
    height: 30px;
  }
  .contacts svg {
    width: 22px;
    height: 22px;
    margin-right: 10px;
    fill: var(--white);
    flex: none;
  }
  .contacts .fax { margin-left: 22px; }
</style>
</head>
<body>
<main class="canvas">

  <section class="card card--front">
    <div class="front-pattern" role="img" aria-label="Faint repeating floral pattern in pale blue-grey"></div>
    <div class="brand">
      <div class="brand__mark"></div>
      <div class="brand__name">Harbourlight<br>Mindcare<br>Studio</div>
    </div>
  </section>

  <section class="card card--back">
    <header class="back-header">
      <h1 class="holder-name">Fiona Kettlewood</h1>
    </header>
    <div class="back-band" role="img" aria-label="Teal band with subtle repeating floral pattern"></div>

    <p class="credentials">
      Clinical Psychologist BPsych,<br>
      BPsych (Hons),<br>
      MPsych (Clin),<br>
      MAPS
    </p>
    <div class="divider"></div>

    <ul class="contacts">
      <li>
        <svg viewBox="0 0 24 24" aria-hidden="true"><path d="M6.6 10.8a15.1 15.1 0 0 0 6.6 6.6l2.2-2.2a1 1 0 0 1 1-.25 11.4 11.4 0 0 0 3.6.57 1 1 0 0 1 1 1V20a1 1 0 0 1-1 1A17 17 0 0 1 3 4a1 1 0 0 1 1-1h3.5a1 1 0 0 1 1 1c0 1.25.2 2.45.57 3.57a1 1 0 0 1-.25 1z"/></svg>
        <span>0457260714</span>
        <svg class="fax" viewBox="0 0 24 24" aria-hidden="true"><path d="M7 2h10v5H7zM4 8h16a2 2 0 0 1 2 2v7h-4v5H6v-5H2v-7a2 2 0 0 1 2-2zm4 8v4h8v-4zm10-5a1 1 0 1 0 0 2 1 1 0 0 0 0-2z"/></svg>
        <span>08 71526804</span>
      </li>
      <li>
        <svg viewBox="0 0 24 24" aria-hidden="true"><path d="M2 5h20v14H2zm2 2v.4l8 5.2 8-5.2V7zm0 2.8V17h16V9.8l-8 5.2z"/></svg>
        <span>hello@harbourlightmindcarestudio.com.au</span>
      </li>
      <li>
        <svg viewBox="0 0 24 24" aria-hidden="true"><path d="M12 2a10 10 0 1 0 0 20 10 10 0 0 0 0-20zm7.9 9h-3.4a15 15 0 0 0-1.4-6.2A8 8 0 0 1 19.9 11zM12 4.1c.9 1.1 2.2 3.6 2.5 6.9h-5c.3-3.3 1.6-5.8 2.5-6.9zM8.9 4.8A15 15 0 0 0 7.5 11H4.1a8 8 0 0 1 4.8-6.2zM4.1 13h3.4a15 15 0 0 0 1.4 6.2A8 8 0 0 1 4.1 13zm7.9 6.9c-.9-1.1-2.2-3.6-2.5-6.9h5c-.3 3.3-1.6 5.8-2.5 6.9zm3.1-.7a15 15 0 0 0 1.4-6.2h3.4a8 8 0 0 1-4.8 6.2z"/></svg>
        <span>harbourlightmindcarestudio.com.au</span>
      </li>
    </ul>
  </section>

</main>
</body>
</html>
```